Banner/Werbemittel für Online-Buchmacher
Zielgruppe
Die galoppfuchs.de AG (ehemals TIPPWERK.DE AG), ansässig in Düsseldorf, hat sich in den vergangenen Jahren zu einer festen Größe im Markt für Pferdewetten in Deutschland etabliert. Das Angebot umfasst dabei insbesondere Online-Pferdewetten, die durch stationäre Pferde-Wettcenter flankiert werden.
Das Flaggschiff der Holding, die Internet-Plattform www.galoppfuchs.de mit mehr als 29.000 registrierten Kunden, zählt zu den Marktführern im Bereich der deutschen Online-Pferdewette. Angeboten werden Wetten auf Pferderennen in 34 Ländern, von denen der überwiegende Teil live im Internet übertragen wird. Dem Nutzer bieten sich ferner über 170.000 archivierte Renn-Videos - das weltweit größte Archiv im Bereich des Pferderennsports. Die Gesellschaft verfügt über in Deutschland und Malta erteilte Lizenzen.
Die galoppfuchs.de AG berät nicht nur ihre Tochtergesellschaften, sondern auch andere in der Wettbranche tätige Firmen und Rennvereine. In ihrer Funktion als Managementholding koordiniert die galoppfuchs.de AG sämtliche Business-Aktivitäten der Tochterunternehmen, etwa der 2009 akquirierten Valmoria GmbH (Essen). Das Systemhaus ist als Berater in allen Fragen der Informations-Technologie unter anderem auf den Vertrieb der von galoppfuchs.de selbstentwickelten Zahlungs- und Webcontent-Systeme für Online-Wetten spezialisiert.
Zielgruppe:
18 - 99 Jahre
Wettaffinität (Sport / Pferderennen)
International
Alle Gehalts- und Bevölkerungsschichten
Aufgabenstellung
Erstellen Sie ansprechende, moderne Banner passend zur Webseite www.galoppfuchs.de für sämtliche Bereiche und in den gängigen Formaten.
Folgende Punkte können mit aufgenommen werden, sind aber nicht Pflicht:
- 100 % Einzahlungsbonus
- Live-Stream weltweit
- mobile Seite
- 24h weltweit wetten
Logo und Produktbilder finden Sie unter "Dateien".
Farbschema: Grau (CMYK 62 56 58 80 / Grün CMYK 56 6 100 0)
Bannerformate:
300x250
120x600
160x600
300x600
300x50
728x90
468x60
234x60
216x36
168x28
120x20

```html
<!DOCTYPE html>
<html lang="de">
<head>
<meta charset="utf-8">
<title>galoppfuchs.de – Bannerformate</title>
<link rel="stylesheet" href="https://fonts.googleapis.com/css2?family=Oswald:wght@400;500;600&family=Open+Sans:wght@400;600;700&display=swap">
<style>
  :root{
    --page:#ffffff;
    --green:#7bb241;
    --green-label:#79ad3e;
    --panel:#141414;
    --frame:#3a3a3a;
    --white:#ffffff;
    --ink:#1b1b1b;
    --photo-top:#6f7782;
    --photo-mid:#6b4a36;
    --photo-low:#3a3430;
    --photo-base:#2a2a2a;
  }
  *{margin:0;padding:0;box-sizing:border-box}
  html,body{width:1200px;height:920px;overflow:hidden;background:var(--page)}
  .sheet{position:relative;width:1200px;height:920px}

  .format-label{
    position:absolute;top:84px;
    font-family:"Oswald",sans-serif;font-weight:500;font-size:26px;
    color:var(--green-label);text-align:center;letter-spacing:.2px;
  }

  .banner{position:absolute;top:136px;overflow:hidden;background:var(--frame)}
  .banner--mrec{left:92px;width:300px;height:250px}
  .banner--half{left:448px;width:300px;height:600px}
  .banner--sky{left:788px;width:120px;height:600px}
  .banner--wide-sky{left:936px;width:160px;height:600px}

  .race-photo{
    position:absolute;inset:0;
    background:
      radial-gradient(ellipse at 55% 60%, rgba(120,78,50,.85) 0%, rgba(90,60,42,.55) 35%, rgba(0,0,0,0) 70%),
      linear-gradient(180deg,var(--photo-top) 0%,var(--photo-top) 25%,var(--photo-mid) 55%,var(--photo-low) 80%,var(--photo-base) 100%);
    filter:saturate(.85) brightness(.85);
  }

  .offer{position:absolute;top:0}
  .offer__head{
    background:var(--green);color:var(--white);text-align:center;
    display:flex;align-items:center;justify-content:center;text-transform:uppercase;
  }
  .offer__body{background:var(--panel);color:var(--white);list-style:none}
  .offer__body li{display:flex;align-items:flex-start}
  .tick{flex:none;fill:none;stroke:var(--green);stroke-linecap:round;stroke-linejoin:round}

  .brand{
    position:absolute;font-family:"Open Sans",sans-serif;font-weight:700;
    color:var(--white);white-space:nowrap;letter-spacing:-.3px;
  }
  .cta{
    position:absolute;background:var(--green);color:var(--ink);border-radius:2px;
    font-family:"Oswald",sans-serif;font-weight:600;font-size:13px;letter-spacing:.4px;
    display:flex;align-items:center;justify-content:center;text-transform:uppercase;
  }

  /* 300x250 */
  .banner--mrec .offer{left:105px;width:189px}
  .banner--mrec .offer__head{height:60px;font-family:"Open Sans",sans-serif;font-size:10.5px;line-height:13px;letter-spacing:.6px;padding:0 4px}
  .banner--mrec .offer__body{height:114px;padding:10px 0 0 12px;font-family:"Open Sans",sans-serif;font-weight:600;font-size:12.5px;line-height:18px;clip-path:polygon(0 0,100% 0,100% 100%,0 78%)}
  .banner--mrec .tick{width:14px;height:14px;margin:2px 4px 0 0;stroke-width:3}
  .banner--mrec .brand{left:8px;top:214px;font-size:21px}
  .banner--mrec .cta{left:202px;top:211px;width:89px;height:29px}

  /* 300x600 */
  .banner--half .offer{left:13px;width:276px}
  .banner--half .offer__head{height:66px;font-family:"Open Sans",sans-serif;font-size:14px;line-height:17px;padding:0 6px}
  .banner--half .offer__head b{font-weight:700}
  .banner--half .offer__body{height:150px;padding:12px 0 0 22px;font-family:"Open Sans",sans-serif;font-size:17px;line-height:24px;clip-path:polygon(0 0,100% 0,100% 100%,0 82%)}
  .banner--half .tick{width:18px;height:18px;margin:3px 4px 0 0;stroke-width:3.4}
  .banner--half .brand{left:0;width:300px;text-align:center;top:514px;font-size:33px}
  .banner--half .cta{left:109px;top:564px;width:90px;height:28px}

  /* 120x600 */
  .banner--sky .offer{left:2px;width:116px}
  .banner--sky .offer__head{height:87px;font-family:"Oswald",sans-serif;font-weight:500;font-size:10.5px;line-height:12.5px;letter-spacing:.5px;padding:0 4px}
  .banner--sky .offer__body{height:180px;padding:16px 0 0 6px;font-family:"Oswald",sans-serif;font-size:12px;line-height:19px;clip-path:polygon(0 0,100% 0,100% 100%,0 93%)}
  .banner--sky .tick{width:9px;height:9px;margin:5px 6px 0 0;stroke-width:3}
  .banner--sky .brand{left:0;width:120px;text-align:center;top:534px;font-size:13px}
  .banner--sky .cta{left:17px;top:563px;width:89px;height:28px}

  /* 160x600 */
  .banner--wide-sky .offer{left:5px;width:150px}
  .banner--wide-sky .offer__head{height:98px;font-family:"Oswald",sans-serif;font-weight:500;font-size:14.5px;line-height:17px;letter-spacing:.7px;padding:0 4px}
  .banner--wide-sky .offer__body{height:148px;padding:20px 0 0 6px;font-family:"Oswald",sans-serif;font-size:12.5px;line-height:19px;clip-path:polygon(0 0,100% 0,100% 100%,0 88%)}
  .banner--wide-sky .tick{width:9px;height:9px;margin:5px 5px 0 0;stroke-width:3}
  .banner--wide-sky .brand{left:0;width:160px;text-align:center;top:522px;font-size:18px}
  .banner--wide-sky .cta{left:37px;top:563px;width:89px;height:28px}
</style>
</head>
<body>
<main class="sheet">
  <svg width="0" height="0" style="position:absolute" aria-hidden="true">
    <symbol id="tick" viewBox="0 0 16 16"><path d="M2 8.5 6 12.5 14 3.5"/></symbol>
  </svg>

  <!-- 300 x 250 -->
  <div class="format-label" style="left:92px;width:300px">300 x 250</div>
  <section class="banner banner--mrec">
    <div class="race-photo" role="img" aria-label="Galopprennen: Jockeys auf Pferden im Rennen"></div>
    <div class="offer">
      <div class="offer__head">Folgende Punkte können<br>mit aufgenommen werden,<br>sind aber nicht Pflicht:</div>
      <ul class="offer__body">
        <li><svg class="tick"><use href="#tick"/></svg>100 % Einzahlungsbonus</li>
        <li><svg class="tick"><use href="#tick"/></svg>Live-Stream weltweit</li>
        <li><svg class="tick"><use href="#tick"/></svg>mobile Seite</li>
        <li><svg class="tick"><use href="#tick"/></svg>24h weltweit wetten</li>
      </ul>
    </div>
    <div class="brand">galoppfuchs.de</div>
    <div class="cta">Click here</div>
  </section>

  <!-- 300 x 600 -->
  <div class="format-label" style="left:448px;width:300px">300x600</div>
  <section class="banner banner--half">
    <div class="race-photo" role="img" aria-label="Galopprennen: Jockeys auf Pferden im Rennen"></div>
    <div class="offer">
      <div class="offer__head"><span><b>Folgende Punkte können</b> mit<br>aufgenommen werden, sind aber<br>nicht Pflicht:</span></div>
      <ul class="offer__body">
        <li><svg class="tick"><use href="#tick"/></svg>100 % Einzahlungsbonus</li>
        <li><svg class="tick"><use href="#tick"/></svg>Live-Stream weltweit</li>
        <li><svg class="tick"><use href="#tick"/></svg>mobile Seite</li>
        <li><svg class="tick"><use href="#tick"/></svg>24h weltweit wetten</li>
      </ul>
    </div>
    <div class="brand">galoppfuchs.de</div>
    <div class="cta">Click here</div>
  </section>

  <!-- 120 x 600 -->
  <div class="format-label" style="left:788px;width:120px">120x600</div>
  <section class="banner banner--sky">
    <div class="race-photo" role="img" aria-label="Galopprennen: Jockeys auf Pferden im Rennen"></div>
    <div class="offer">
      <div class="offer__head">Folgende Punkte<br>können mit<br>aufgenommen<br>werden,sind<br>aber nicht Pflicht:</div>
      <ul class="offer__body">
        <li><svg class="tick"><use href="#tick"/></svg><span>100 %<br>Einzahlungsbonus</span></li>
        <li><svg class="tick"><use href="#tick"/></svg><span>Live-Stream<br>weltweit</span></li>
        <li><svg class="tick"><use href="#tick"/></svg>mobile Seite</li>
        <li><svg class="tick"><use href="#tick"/></svg><span>24h weltweit<br>wetten</span></li>
      </ul>
    </div>
    <div class="brand">galoppfuchs.de</div>
    <div class="cta">Click here</div>
  </section>

  <!-- 160 x 600 -->
  <div class="format-label" style="left:936px;width:160px">160x600</div>
  <section class="banner banner--wide-sky">
    <div class="race-photo" role="img" aria-label="Galopprennen: Jockeys auf Pferden im Rennen"></div>
    <div class="offer">
      <div class="offer__head">Folgende Punkte<br>können mit<br>aufgenommen<br>werden,sind<br>aber nicht Pflicht:</div>
      <ul class="offer__body">
        <li><svg class="tick"><use href="#tick"/></svg>100 % Einzahlungsbonus</li>
        <li><svg class="tick"><use href="#tick"/></svg>Live-Stream weltweit</li>
        <li><svg class="tick"><use href="#tick"/></svg>mobile Seite</li>
        <li><svg class="tick"><use href="#tick"/></svg>24h weltweit wetten</li>
      </ul>
    </div>
    <div class="brand">galoppfuchs.de</div>
    <div class="cta">Click here</div>
  </section>
</main>
</body>
</html>
```